Signage Design Project

We are a chiropractic clinic that caters mostly to athletes. We've recently purchased the first whole body cryotherapy unit in San Antonio, TX (for commercial use - the SA Falcons have a unit for their facility) that we would like to advertise in window signage. Please refer to frostlane.com & glacierwell.com to get more info about this service. Our focus is recovery, injury therapy, performance enhancement, metabolic & immunity boost, rheumatoid diseases & pain management, anti-aging & skin rejuvenation. Window measures approximately 8'8" X 3'2"
We mostly use the horizontal logo format (attached) in black & blue.
Industry/Entity Type
Clinic
Requirements
Must have
- Website: www.pelwickback.com
Logo (attached)
"JUST 3 MINUTES FOR WHOLE BODY RECOVERY"
"Whole Body Cryotherapy"
*recovery
*injury therapy
*performance enhancement
*metabolic & immunity boost
*rheumatoid diseases
*pain management
*anti-aging
*skin rejuvenation
Nice to have
- image of Cryo unit (attached)
image of an athlete(s) similar to the ones attached

```html
<!DOCTYPE html>
<html lang="en">
<head>
<meta charset="utf-8">
<title>Pelwick Sport &amp; Spine – Whole Body Cryotherapy</title>
<link rel="stylesheet" href="https://fonts.googleapis.com/css2?family=PT+Sans:wght@700&family=Montserrat:wght@500&display=swap">
<style>
  :root {
    --brand-blue: #1ea6e3;
    --ink: #141414;
    --paper: #ffffff;
    --sun-light: #fbe3a6;
    --sun-mid: #f2b765;
    --sun-deep: #b9662a;
    --unit-steel: #5d6066;
    --unit-light: #a4a7ad;
    --band: rgba(255, 255, 255, 0.72);
  }
  * { margin: 0; padding: 0; box-sizing: border-box; }
  html, body { width: 1200px; height: 758px; overflow: hidden; background: var(--paper); }
  .sign {
    position: relative;
    width: 1200px;
    height: 758px;
    overflow: hidden;
    background: var(--paper);
    font-family: "PT Sans", Arial, sans-serif;
  }
  .scene-photo {
    position: absolute;
    left: 62px; top: 0;
    width: 1138px; height: 758px;
    background:
      radial-gradient(ellipse 45% 38% at 62% 42%, #fff6d8 0%, rgba(255,246,216,0) 70%),
      linear-gradient(180deg, #fdf3d6 0%, var(--sun-light) 35%, var(--sun-mid) 62%, #e9c487 80%, var(--sun-deep) 100%);
  }
  .runner-photo {
    position: absolute;
    left: 548px; top: 176px;
    width: 210px; height: 420px;
    border-radius: 90px 90px 40px 40px;
    background: linear-gradient(180deg, rgba(214,150,88,0.35), rgba(176,108,52,0.28));
  }
  .cryo-unit {
    position: absolute;
    left: 144px; top: 124px;
    width: 296px; height: 560px;
    border-radius: 40px 40px 14px 14px;
    background: linear-gradient(90deg, var(--unit-steel) 0%, var(--unit-light) 45%, var(--unit-steel) 100%);
  }
  .headline {
    position: absolute;
    left: 378px; top: 26px;
    width: 800px;
    text-align: center;
    color: var(--brand-blue);
    font-weight: 700;
    text-transform: uppercase;
    line-height: 1;
  }
  .headline .line-one { display: block; font-size: 52px; letter-spacing: 0.5px; }
  .headline .line-two { display: block; font-size: 55px; margin-top: 6px; letter-spacing: 0.5px; }
  .service-title {
    position: absolute;
    left: 776px; top: 184px;
    font-size: 32px;
    color: var(--ink);
    font-weight: 700;
  }
  .benefit-list {
    position: absolute;
    left: 774px; top: 228px;
    list-style: none;
    font-size: 26px;
    line-height: 32px;
    color: var(--ink);
    font-weight: 700;
  }
  .footer-band {
    position: absolute;
    left: 62px; top: 540px;
    width: 1138px; height: 180px;
    background: var(--band);
  }
  .brand {
    position: absolute;
    left: 680px; top: 584px;
    display: flex;
    align-items: center;
    gap: 18px;
    color: var(--brand-blue);
    font-family: "Montserrat", Arial, sans-serif;
    font-weight: 500;
  }
  .brand-mark {
    width: 52px; height: 52px;
    background: var(--brand-blue);
  }
  .brand-name { line-height: 1; }
  .brand-name .primary { display: block; font-size: 38px; letter-spacing: 5px; }
  .brand-name .secondary { display: block; font-size: 21px; letter-spacing: 3px; margin-top: 6px; }
  .web-address {
    position: absolute;
    left: 446px; top: 666px;
    font-size: 43px;
    color: var(--brand-blue);
    font-weight: 700;
  }
</style>
</head>
<body>
  <main class="sign">
    <div class="scene-photo" role="img" aria-label="Sunlit riverside path with a city skyline at golden hour"></div>
    <div class="runner-photo" role="img" aria-label="Female athlete jogging along the river path"></div>
    <div class="cryo-unit" role="img" aria-label="Whole body cryotherapy chamber with perforated steel panels and vapour rising from the top"></div>

    <h1 class="headline">
      <span class="line-one">Just 3 minutes</span>
      <span class="line-two">for whole body recovery!</span>
    </h1>

    <h2 class="service-title">Whole Body Cryotherapy</h2>
    <ul class="benefit-list">
      <li>*recovery</li>
      <li>*injury therapy</li>
      <li>*performance enhancement</li>
      <li>*metabolic &amp; immunity boost</li>
      <li>*rheumatoid diseases</li>
      <li>*pain management</li>
      <li>*anti-aging</li>
      <li>*skin rejuvenation</li>
    </ul>

    <div class="footer-band"></div>
    <div class="brand">
      <span class="brand-mark"></span>
      <span class="brand-name">
        <span class="primary">PELWICK</span>
        <span class="secondary">SPORT &amp; SPINE</span>
      </span>
    </div>
    <p class="web-address">Visit us at www.pelwickback.com</p>
  </main>
</body>
</html>
```